Power point design for a financial seminar

I would like to receive 10 designed power point slides with the same look & feel that should related to finance since its for a seminar related to stock markets and economics. Please note that texts are in Hebrew (translate is attached in a Word document).
There should be background with upper and bottom layers similar to all to include the attached logo.
All slides should have a Title and some of the slides should have designed bullets and other generic graphic elements that we will use in our presentation.
Please note that text should be right to left so texts will be aligned to the right and graphics at the left/upper/bottom
Youngsters

```html
<!DOCTYPE html>
<html lang="he" dir="rtl">
<head>
<meta charset="utf-8">
<title>קורס שוק ההון – בסיס</title>
<link href="https://fonts.googleapis.com/css2?family=Heebo:wght@400;500;700;800&display=swap" rel="stylesheet">
<style>
:root{
  --navy:#0a3d8f;
  --blue:#1565c8;
  --sky:#3b8ee6;
  --pale:#e6f0fb;
  --mist:#f2f6fb;
  --green:#35c28f;
  --ink:#23324a;
  --muted:#6b7a90;
  --stage:#e9eef5;
}
*{box-sizing:border-box;margin:0;padding:0}
html,body{width:1200px;height:2708px;overflow:hidden}
body{background:var(--stage);font-family:'Heebo',sans-serif;color:var(--ink);position:relative}
.slide{position:absolute;background:#fff;overflow:hidden;box-shadow:0 4px 14px rgba(20,50,100,.12);border-radius:4px}
.slide::after{content:"";position:absolute;left:0;right:0;bottom:0;height:14px;background:linear-gradient(90deg,var(--sky),var(--pale) 60%,#fff)}
.slide::before{content:"";position:absolute;left:0;top:0;width:100%;height:6px;background:linear-gradient(270deg,var(--blue),var(--pale))}
.slide-title{position:absolute;top:20px;right:26px;font-size:17px;font-weight:800;color:var(--navy)}
.logo-tab{position:absolute;top:0;left:50%;transform:translateX(-50%);background:#fff;border-radius:0 0 10px 10px;box-shadow:0 3px 8px rgba(20,50,100,.15);padding:6px 10px;display:flex;align-items:center;gap:5px;font-size:9px;font-weight:700;color:var(--navy);z-index:2}
.logo-dot{width:12px;height:12px;border-radius:50%;background:var(--blue)}
/* title slide */
.cover{background:linear-gradient(180deg,var(--navy),var(--blue) 55%,var(--sky))}
.cover::before{background:rgba(255,255,255,.15)}
.cover::after{background:linear-gradient(90deg,rgba(255,255,255,.35),rgba(255,255,255,0))}
.cover-texture{position:absolute;inset:0;background:linear-gradient(120deg,rgba(255,255,255,.06),rgba(255,255,255,0) 50%,rgba(255,255,255,.08))}
.cover-logo{position:absolute;top:0;left:50%;transform:translateX(-50%);background:#fff;border-radius:0 0 16px 16px;box-shadow:0 6px 16px rgba(0,0,0,.2);display:flex;flex-direction:column;align-items:center;justify-content:center;font-weight:700;color:var(--navy)}
.cover-logo .logo-dot{background:var(--blue)}
.cover-title{position:absolute;width:100%;text-align:center;color:#fff;font-weight:800}
.presenter{position:absolute;left:50%;transform:translateX(-50%);background:var(--green);color:#fff;font-weight:700;border-radius:999px;text-align:center}
/* bullets */
.bullets{position:absolute;list-style:none;display:flex;flex-direction:column;gap:9px}
.bullets li{display:flex;align-items:center;gap:8px;font-size:11px;background:var(--mist);border-radius:4px;padding:5px 8px}
.bullets li::before{content:"";width:10px;height:10px;border-radius:2px;background:var(--blue);flex:none}
.photo{position:absolute;border-radius:6px;background:linear-gradient(135deg,#7fa8d8,#2f5f9e 60%,#1b3f73)}
.icon-box{width:26px;height:26px;border-radius:5px;background:var(--blue);display:flex;align-items:center;justify-content:center;flex:none}
.icon-box svg{width:14px;height:14px;stroke:#fff;fill:none;stroke-width:2}
.icon-box.alt{background:var(--green)}
.card-grid{position:absolute;display:grid;gap:10px}
.card{background:#fff;border:1px solid #dbe6f3;border-radius:5px;padding:8px;font-size:10px;display:flex;flex-direction:column;gap:6px;box-shadow:0 2px 5px rgba(20,50,100,.06)}
.card .icon-box{width:20px;height:20px}
.metric{background:#fff;border:1px solid #dbe6f3;border-radius:5px;padding:10px;font-size:10px;position:relative;overflow:hidden}
.metric::before{content:"";position:absolute;left:0;top:0;width:26px;height:26px;background:var(--blue);border-radius:0 0 8px 0}
.metric b{display:block;color:var(--navy);font-size:11px;margin-bottom:3px}
.row-item{display:flex;align-items:center;gap:8px;font-size:10.5px}
.caption{position:absolute;color:#fff;font-weight:700;font-size:13px}
.label{position:absolute;font-size:10.5px;font-weight:500}
</style>
</head>
<body>

<!-- hero -->
<section class="slide cover" style="left:150px;top:190px;width:900px;height:520px">
  <div class="cover-texture"></div>
  <div class="cover-logo" style="width:150px;height:90px;gap:6px;font-size:14px">
    <span class="logo-dot" style="width:30px;height:30px"></span>מרכז ההשקעות
  </div>
  <h1 class="cover-title" style="top:210px;font-size:46px">קורס שוק ההון- בסיס (חדש)</h1>
  <div class="presenter" style="top:300px;width:220px;padding:10px 0;font-size:18px">נועם לוי</div>
</section>

<!-- title slide -->
<section class="slide cover" style="left:32px;top:1010px;width:1136px;height:300px">
  <div class="cover-texture"></div>
  <div class="cover-logo" style="width:120px;height:68px;gap:4px;font-size:12px">
    <span class="logo-dot" style="width:22px;height:22px"></span>מרכז ההשקעות
  </div>
  <h1 class="cover-title" style="top:120px;font-size:36px">קורס שוק ההון- בסיס (חדש)</h1>
  <div class="presenter" style="top:185px;width:180px;padding:8px 0;font-size:15px">נועם לוי</div>
</section>

<!-- goals -->
<section class="slide" style="left:32px;top:1322px;width:560px;height:262px">
  <div class="logo-tab"><span class="logo-dot"></span>מרכז ההשקעות</div>
  <h2 class="slide-title">יעד הסדרה</h2>
  <ul class="bullets" style="top:56px;right:26px;width:320px">
    <li>נבין את התהליכים בשוק ההון</li>
    <li>נכיר מושגי יסוד בהשקעות</li>
    <li>נלמד לקרוא דוחות כספיים</li>
    <li>נבנה תיק השקעות ראשון</li>
    <li>נכיר כלים לניהול סיכונים</li>
  </ul>
  <div class="photo" role="img" aria-label="תמונת גרף מניות על מסך" style="left:24px;top:56px;width:170px;height:170px"></div>
</section>

<!-- image slide -->
<section class="slide" style="left:608px;top:1322px;width:560px;height:262px">
  <div class="logo-tab"><span class="logo-dot"></span>מרכז ההשקעות</div>
  <div class="photo" role="img" aria-label="תמונת לחיצת ידיים בפגישה עסקית" style="left:24px;top:48px;width:512px;height:186px"></div>
</section>

<!-- five factors -->
<section class="slide" style="left:32px;top:1596px;width:560px;height:262px">
  <div class="logo-tab"><span class="logo-dot"></span>מרכז ההשקעות</div>
  <h2 class="slide-title">5 גורמים בהרצאה</h2>
  <svg width="150" height="150" viewBox="0 0 150 150" style="position:absolute;left:205px;top:60px">
    <circle cx="75" cy="75" r="55" fill="none" stroke="#1565c8" stroke-width="34" stroke-dasharray="62 7.1"/>
    <circle cx="75" cy="75" r="55" fill="none" stroke="#0a3d8f" stroke-width="34" stroke-dasharray="62 283.6" stroke-dashoffset="-138.2"/>
    <circle cx="75" cy="75" r="30" fill="#fff"/>
    <circle cx="75" cy="75" r="20" fill="#e6f0fb"/>
    <path d="M66 82 l6-8 5 4 8-10" stroke="#1565c8" stroke-width="2.5" fill="none"/>
  </svg>
  <span class="label" style="right:215px;top:58px">מחיר המניה</span>
  <span class="label" style="right:90px;top:118px">אנליזה</span>
  <span class="label" style="right:150px;top:210px">קרנות נאמנות</span>
  <span class="label" style="left:150px;top:210px">הנהלה</span>
  <span class="label" style="left:110px;top:118px">סקטור</span>
</section>

<!-- definitions -->
<section class="slide" style="left:608px;top:1596px;width:560px;height:262px">
  <div class="logo-tab"><span class="logo-dot"></span>מרכז ההשקעות</div>
  <h2 class="slide-title">הגדרות</h2>
  <div class="card-grid" style="top:60px;right:26px;left:26px;grid-template-columns:repeat(4,1fr)">
    <div class="card"><span class="icon-box"><svg viewBox="0 0 14 14"><path d="M2 11l4-4 3 2 4-6"/></svg></span>מניה היא חלק מחברה</div>
    <div class="card"><span class="icon-box"><svg viewBox="0 0 14 14"><circle cx="7" cy="7" r="5"/></svg></span>אג"ח היא הלוואה לחברה</div>
    <div class="card"><span class="icon-box"><svg viewBox="0 0 14 14"><path d="M2 12V6M7 12V3M12 12V8"/></svg></span>מדד מודד קבוצת מניות</div>
    <div class="card"><span class="icon-box"><svg viewBox="0 0 14 14"><path d="M3 7l3 3 5-6"/></svg></span>דיבידנד הוא חלוקת רווח</div>
  </div>
</section>

<!-- stock price -->
<section class="slide" style="left:32px;top:1870px;width:560px;height:262px">
  <div class="logo-tab"><span class="logo-dot"></span>מרכז ההשקעות</div>
  <h2 class="slide-title">המשך: על מחיר המניה</h2>
  <ul class="bullets" style="top:56px;right:26px;width:240px;gap:7px">
    <li>היצע וביקוש</li>
    <li>תוצאות כספיות</li>
    <li>ציפיות המשקיעים</li>
    <li>ריבית ואינפלציה</li>
    <li>חדשות ואירועים</li>
  </ul>
  <ul class="bullets" style="top:56px;left:26px;width:230px;gap:7px">
    <li>שווי שוק</li>
    <li>מכפיל רווח</li>
    <li>תשואה לבעלי המניות</li>
  </ul>
</section>

<!-- indices -->
<section class="slide" style="left:608px;top:1870px;width:560px;height:262px">
  <div class="logo-tab"><span class="logo-dot"></span>מרכז ההשקעות</div>
  <h2 class="slide-title">מדדים</h2>
  <div class="card-grid" style="top:58px;right:26px;left:26px;grid-template-columns:1fr 1fr">
    <div class="metric"><b>מדד מניות מוביל</b>35 החברות הגדולות בבורסה</div>
    <div class="metric"><b>מדד מניות רחב</b>125 החברות הגדולות בבורסה</div>
    <div class="metric"><b>מדד אג"ח</b>אגרות חוב ממשלתיות וקונצרניות</div>
    <div class="metric"><b>מדד בינלאומי</b>מניות מובילות בשווקים בעולם</div>
  </div>
</section>

<!-- how to invest -->
<section class="slide" style="left:32px;top:2144px;width:560px;height:262px">
  <div class="logo-tab"><span class="logo-dot"></span>מרכז ההשקעות</div>
  <h2 class="slide-title">איך להשקיע</h2>
  <svg width="500" height="140" viewBox="0 0 500 140" style="position:absolute;left:30px;top:70px">
    <path d="M10 70 C80 10 120 130 190 70 S300 10 320 70 S430 130 490 70" fill="none" stroke="#3b8ee6" stroke-width="6"/>
    <g fill="#1565c8">
      <rect x="60" y="48" width="40" height="40" rx="6" transform="rotate(45 80 68)"/>
      <rect x="170" y="50" width="40" height="40" rx="6" transform="rotate(45 190 70)"/>
      <rect x="290" y="50" width="40" height="40" rx="6" transform="rotate(45 310 70)"/>
      <rect x="400" y="52" width="40" height="40" rx="6" transform="rotate(45 420 72)"/>
    </g>
    <g stroke="#fff" stroke-width="2.5" fill="none">
      <path d="M72 72l6 5 10-12"/><circle cx="190" cy="70" r="7"/><path d="M302 74l8-8 8 8"/><path d="M412 72h16"/>
    </g>
  </svg>
  <span class="label" style="left:90px;top:218px">מעקב שוטף</span>
  <span class="label" style="left:200px;top:96px">רכישה</span>
  <span class="label" style="right:190px;top:218px">בחירה</span>
  <span class="label" style="right:40px;top:96px">ניתוח</span>
</section>

<!-- parameters -->
<section class="slide" style="left:608px;top:2144px;width:560px;height:262px">
  <div class="logo-tab"><span class="logo-dot"></span>מרכז ההשקעות</div>
  <h2 class="slide-title">פרמטרים להשקעה</h2>
  <div class="card-grid" style="top:62px;right:26px;left:40px;grid-template-columns:1fr 1fr;gap:16px 30px">
    <div class="row-item"><span class="icon-box"><svg viewBox="0 0 14 14"><path d="M2 11l4-4 3 2 4-6"/></svg></span>טווח ההשקעה</div>
    <div class="row-item"><span class="icon-box"><svg viewBox="0 0 14 14"><circle cx="7" cy="7" r="5"/></svg></span>רמת סיכון</div>
    <div class="row-item"><span class="icon-box"><svg viewBox="0 0 14 14"><path d="M2 12V6M7 12V3M12 12V8"/></svg></span>נזילות</div>
    <div class="row-item"><span class="icon-box"><svg viewBox="0 0 14 14"><path d="M3 7l3 3 5-6"/></svg></span>פיזור</div>
    <div class="row-item"><span class="icon-box"><svg viewBox="0 0 14 14"><path d="M2 7h10M7 2v10"/></svg></span>עמלות</div>
    <div class="row-item"><span class="icon-box"><svg viewBox="0 0 14 14"><rect x="2" y="3" width="10" height="8"/></svg></span>מיסוי</div>
  </div>
</section>

<!-- financial assets -->
<section class="slide" style="left:32px;top:2418px;width:560px;height:262px">
  <div class="logo-tab"><span class="logo-dot"></span>מרכז ההשקעות</div>
  <h2 class="slide-title">נכסים פיננסים</h2>
  <div class="photo" role="img" aria-label="תמונת פגישת ייעוץ השקעות" style="right:26px;top:58px;width:245px;height:170px"></div>
  <div class="photo" role="img" aria-label="תמונת לחיצת ידיים עסקית" style="left:26px;top:58px;width:245px;height:170px"></div>
  <span class="caption" style="right:44px;top:200px">תיקים אקטיביים</span>
  <span class="caption" style="left:190px;top:200px">אחזקות</span>
</section>

<!-- advanced topics -->
<section class="slide" style="left:608px;top:2418px;width:560px;height:262px">
  <div class="logo-tab"><span class="logo-dot"></span>מרכז ההשקעות</div>
  <h2 class="slide-title">נושאים מתקדמים</h2>
  <div class="card-grid" style="top:62px;right:26px;left:26px;grid-template-columns:repeat(3,1fr);gap:14px">
    <div class="card" style="flex-direction:row;align-items:center"><span class="icon-box"><svg viewBox="0 0 14 14"><path d="M2 11l4-4 3 2 4-6"/></svg></span>ניתוח טכני</div>
    <div class="card" style="flex-direction:row;align-items:center"><span class="icon-box alt"><svg viewBox="0 0 14 14"><circle cx="7" cy="7" r="5"/></svg></span>אופציות</div>
    <div class="card" style="flex-direction:row;align-items:center"><span class="icon-box"><svg viewBox="0 0 14 14"><path d="M2 12V6M7 12V3M12 12V8"/></svg></span>ניתוח דוחות</div>
    <div class="card" style="flex-direction:row;align-items:center"><span class="icon-box alt"><svg viewBox="0 0 14 14"><path d="M3 7l3 3 5-6"/></svg></span>קרנות סל</div>
    <div class="card" style="flex-direction:row;align-items:center"><span class="icon-box"><svg viewBox="0 0 14 14"><path d="M2 7h10M7 2v10"/></svg></span>שוק ההון בעולם</div>
    <div class="card" style="flex-direction:row;align-items:center"><span class="icon-box alt"><svg viewBox="0 0 14 14"><rect x="2" y="3" width="10" height="8"/></svg></span>מטבעות</div>
  </div>
</section>

</body>
</html>
```